Business Cards for a law firm

Business cards for our law firm. Use our silhoette logo and OAK HARBOR - check our website (www.oakharbor-legal.com)

Contact Information for Business Card

our silhouette logo, OAK HARBOR, 800-555-0147, Dorian Kestrup, dorian@oakharbor-legal.com

Requirements
Must have
• our silhouette logo, OAK HARBOR, 800-555-0147, Dorian Kestrup, dorian@oakharbor-legal.com

```html
<!DOCTYPE html>
<html lang="en">
<head>
<meta charset="utf-8">
<title>Oak Harbor – Business Cards</title>
<link rel="stylesheet" href="https://fonts.googleapis.com/css2?family=Lato:wght@400;700;900&display=swap">
<style>
  :root {
    --stage: #1f1f1f;
    --navy: #1b3270;
    --navy-mark: #1e3477;
    --white: #ffffff;
    --orange: #f6a21c;
    --ink: #1c2a55;
    --ghost: #e9ebf2;
    --silver: #d9dce3;
  }
  * { margin: 0; padding: 0; box-sizing: border-box; }
  html, body { width: 1200px; height: 977px; overflow: hidden; }
  body {
    background: var(--stage);
    font-family: "Lato", sans-serif;
    position: relative;
  }
  .card {
    position: absolute;
    width: 540px;
    height: 310px;
    border-radius: 18px;
    overflow: hidden;
  }
  /* Front */
  .card--front {
    left: 90px; top: 110px;
    background: var(--navy);
    display: flex; align-items: center; justify-content: center;
  }
  .brand {
    display: flex; align-items: center; gap: 16px;
  }
  .brand__dot {
    width: 22px; height: 22px; border-radius: 50%;
    background: var(--silver);
  }
  .brand__name {
    color: var(--silver);
    font-weight: 400;
    font-size: 38px;
    letter-spacing: 5px;
  }
  /* Back */
  .card--back {
    left: 570px; top: 540px;
    background: var(--white);
  }
  .accent-bar {
    position: absolute; left: 0; top: 150px;
    width: 8px; height: 118px;
    background: var(--orange);
  }
  .identity {
    position: absolute; left: 44px; top: 120px;
  }
  .identity__name {
    color: var(--ink);
    font-weight: 900;
    font-size: 27px;
    letter-spacing: 0.5px;
    text-transform: uppercase;
  }
  .identity__role {
    color: var(--orange);
    font-size: 16px;
    margin-top: 2px;
  }
  .contacts {
    position: absolute; left: 44px; top: 196px;
    list-style: none;
  }
  .contacts li {
    display: flex; align-items: center; gap: 10px;
    color: var(--ink);
    font-size: 14px;
    line-height: 24px;
  }
  .contacts svg { width: 12px; height: 12px; fill: var(--ink); flex: none; }
  .figure-area {
    position: absolute; right: 30px; top: 22px;
    width: 210px; height: 250px;
    border-radius: 6px;
    background: linear-gradient(160deg, #2a438a, var(--navy-mark));
  }
  .ghost-name {
    position: absolute; left: 22px; bottom: 8px;
    color: var(--ghost);
    font-weight: 900;
    font-size: 62px;
    letter-spacing: 6px;
    white-space: nowrap;
  }
</style>
</head>
<body>

  <section class="card card--front">
    <div class="brand">
      <span class="brand__dot"></span>
      <span class="brand__name">OAK HARBOR</span>
    </div>
  </section>

  <section class="card card--back">
    <div class="ghost-name">OAK HARBOR</div>
    <div class="figure-area" role="img" aria-label="Two standing figures in navy silhouette"></div>
    <span class="accent-bar"></span>
    <div class="identity">
      <h1 class="identity__name">Dorian Kestrup</h1>
      <p class="identity__role">Attorney</p>
    </div>
    <ul class="contacts">
      <li>
        <svg viewBox="0 0 24 24"><path d="M6.6 10.8a15.1 15.1 0 0 0 6.6 6.6l2.2-2.2c.3-.3.7-.4 1-.2 1.1.4 2.3.6 3.6.6.6 0 1 .4 1 1V20c0 .6-.4 1-1 1A17 17 0 0 1 3 4c0-.6.4-1 1-1h3.5c.6 0 1 .4 1 1 0 1.3.2 2.5.6 3.6.1.3 0 .7-.2 1z"/></svg>
        (800) 555-0147
      </li>
      <li>
        <svg viewBox="0 0 24 24"><path d="M2 5h20v14H2zm2 2v.4l8 5 8-5V7zm0 2.8V17h16V9.8l-8 5z"/></svg>
        dorian@oakharbor-legal.com
      </li>
      <li>
        <svg viewBox="0 0 24 24"><circle cx="12" cy="12" r="10"/></svg>
        www.oakharbor-legal.com
      </li>
    </ul>
  </section>

</body>
</html>
```